BRV Business Cards
Business Cards
BRV Business Cards - Security
Creative Brief
Professional
Daniel Forster
President
742 Larkfield Road Edison, NJ 08841
d.forster@brv-inc.example
www.brv-inc.example

```html
<!DOCTYPE html>
<html lang="en">
<head>
<meta charset="utf-8">
<title>BRV Stationery Set</title>
<link href="https://fonts.googleapis.com/css2?family=Libre+Baskerville:wght@700&family=Open+Sans:wght@400;600&display=swap" rel="stylesheet">
<style>
:root{
  --stage-light:#d2d2d2;
  --stage-dark:#8c8c8c;
  --paper:#ffffff;
  --navy:#0d2a6b;
  --blue:#1f4fa8;
  --steel:#9aa3b3;
  --ink:#3a3f4a;
  --faint:#eef0f4;
  --label:#4a4a4a;
}
*{margin:0;padding:0;box-sizing:border-box}
html,body{width:1200px;height:444px;overflow:hidden}
body{position:relative;background:radial-gradient(ellipse at 50% 45%,var(--stage-light),var(--stage-dark));font-family:"Open Sans",Arial,sans-serif;color:var(--ink)}
.sheet{position:absolute;background:var(--paper);box-shadow:0 3px 8px rgba(0,0,0,.35);overflow:hidden}
.wave{position:absolute;left:0;bottom:0;width:100%;display:block}
.label{position:absolute;font-size:6px;color:var(--label);text-align:center;white-space:nowrap}
.brand{display:flex;align-items:center;gap:4px}
.brand .mark{border-radius:50%;background:var(--navy);flex:none}
.brand .name{font-family:"Libre Baskerville",Georgia,serif;font-weight:700;color:var(--navy);letter-spacing:.5px;line-height:1}
.brand.light .mark{background:#fff}
.brand.light .name{color:#fff}
.contact{position:absolute;font-size:4.5px;line-height:1.45;color:var(--ink);white-space:nowrap}
.watermark{position:absolute;left:50%;top:46%;transform:translate(-50%,-50%);width:160px;height:160px;border-radius:50%;border:13px solid var(--faint);display:flex;align-items:center;justify-content:center}
.watermark span{font-family:"Libre Baskerville",Georgia,serif;font-weight:700;font-size:34px;color:var(--faint)}
.card{width:168px;height:86px;left:19px}
.card-back{background:linear-gradient(135deg,var(--navy),var(--blue))}
.person{position:absolute;left:12px;top:38px;font-size:5px;line-height:1.4}
.person strong{font-family:"Libre Baskerville",Georgia,serif;font-size:6.5px;color:var(--navy)}
.brand-stack{display:flex;flex-direction:column;gap:3px}
.brand-stack .web{font-size:5px;color:var(--ink)}
.letterhead{top:12px;width:268px;height:400px}
.envelope{left:816px;width:365px;height:76px}
.flap{position:absolute;left:0;top:0;width:100%;height:100%;display:block}
</style>
</head>
<body>

<!-- Business card front -->
<div class="sheet card" style="top:100px">
  <div class="brand" style="position:absolute;left:10px;top:10px"><span class="mark" style="width:9px;height:9px"></span><span class="name" style="font-size:10px">BRV</span></div>
  <div class="person"><strong>Daniel Forster</strong><br>President</div>
  <div class="contact" style="right:10px;top:10px;text-align:right">742 Larkfield Road<br>Edison, NJ 08841<br>(732) 555-0187<br>d.forster@brv-inc.example<br>www.brv-inc.example</div>
  <svg class="wave" viewBox="0 0 168 30" height="30" preserveAspectRatio="none"><path d="M0 30 L0 27 Q84 30 168 3 L168 30Z" fill="var(--steel)"/><path d="M30 30 Q105 27 168 9 L168 30Z" fill="var(--navy)"/></svg>
</div>
<div class="label" style="left:19px;top:190px;width:168px">Front card</div>

<!-- Business card back, option 1 -->
<div class="sheet card card-back" style="top:200px">
  <div class="brand light" style="position:absolute;left:50%;top:50%;transform:translate(-50%,-50%)"><span class="mark" style="width:12px;height:12px"></span><span class="name" style="font-size:13px">BRV</span></div>
</div>
<div class="label" style="left:19px;top:291px;width:168px">Back card option 1</div>

<!-- Business card back, option 2 -->
<div class="sheet card" style="top:312px">
  <div class="brand" style="position:absolute;left:14px;top:50%;transform:translateY(-50%);gap:6px">
    <span class="mark" style="width:28px;height:28px"></span>
    <div class="brand-stack"><span class="name" style="font-size:12px">BRV</span><span class="web">www.brv-inc.example</span></div>
  </div>
</div>
<div class="label" style="left:19px;top:403px;width:168px">Back card option 2</div>

<!-- Letterhead 1 -->
<div class="sheet letterhead" style="left:202px">
  <div class="brand" style="position:absolute;left:16px;top:16px"><span class="mark" style="width:14px;height:14px"></span><span class="name" style="font-size:14px">BRV</span></div>
  <div class="contact" style="left:150px;top:15px">742 Larkfield Road Edison, NJ 08841<br>(732) 555-0187<br>www.brv-inc.example</div>
  <div class="watermark"><span>BRV</span></div>
  <svg class="wave" viewBox="0 0 205 46" height="60" preserveAspectRatio="none"><path d="M0 14 Q90 40 205 8 L205 46 L0 46Z" fill="var(--steel)"/><path d="M0 22 Q100 44 205 16 L205 46 L0 46Z" fill="var(--blue)"/><path d="M0 30 Q110 46 205 26 L205 46 L0 46Z" fill="var(--navy)"/></svg>
</div>
<div class="label" style="left:202px;top:418px;width:268px">Letterhead option 1</div>

<!-- Letterhead 2 -->
<div class="sheet letterhead" style="left:504px">
  <div class="brand" style="position:absolute;left:16px;top:16px"><span class="mark" style="width:14px;height:14px"></span><span class="name" style="font-size:14px">BRV</span></div>
  <div class="contact" style="left:150px;top:15px">742 Larkfield Road Edison, NJ 08841<br>(732) 555-0187<br>www.brv-inc.example</div>
  <div class="watermark"><span>BRV</span></div>
  <svg class="wave" viewBox="0 0 205 46" height="60" preserveAspectRatio="none"><path d="M0 8 Q110 40 205 14 L205 46 L0 46Z" fill="var(--steel)"/><path d="M0 16 Q105 44 205 22 L205 46 L0 46Z" fill="var(--blue)"/><path d="M0 26 Q95 46 205 30 L205 46 L0 46Z" fill="var(--navy)"/></svg>
</div>
<div class="label" style="left:504px;top:418px;width:268px">Letterhead option 2</div>

<!-- Envelope back, grey flap -->
<div class="sheet envelope" style="top:40px">
  <svg class="flap" viewBox="0 0 290 84" preserveAspectRatio="none"><path d="M0 0 L290 0 L290 20 L145 48 L0 20Z" fill="#7d828c"/></svg>
  <div class="brand" style="position:absolute;left:50%;top:52px;transform:translateX(-50%)"><span class="mark" style="width:9px;height:9px"></span><span class="name" style="font-size:9px">BRV</span></div>
</div>

<!-- Envelope back, blue flap -->
<div class="sheet envelope" style="top:124px">
  <svg class="flap" viewBox="0 0 290 84" preserveAspectRatio="none"><path d="M0 0 L290 0 L290 14 L145 46 L0 14Z" fill="var(--navy)"/><path d="M0 14 L145 46 L290 14 L290 20 L145 52 L0 20Z" fill="var(--steel)"/></svg>
  <div class="brand" style="position:absolute;left:50%;top:55px;transform:translateX(-50%)"><span class="mark" style="width:9px;height:9px"></span><span class="name" style="font-size:9px">BRV</span></div>
</div>

<!-- Envelope front 1 -->
<div class="sheet envelope" style="top:208px">
  <div class="brand" style="position:absolute;left:10px;top:9px"><span class="mark" style="width:9px;height:9px"></span><span class="name" style="font-size:9px">BRV</span></div>
  <div class="contact" style="left:10px;top:22px">742 Larkfield Road Edison, NJ 08841</div>
  <svg class="wave" viewBox="0 0 290 20" height="20" preserveAspectRatio="none"><path d="M0 20 L0 14 Q150 22 290 4 L290 20Z" fill="var(--steel)"/><path d="M60 20 Q180 18 290 10 L290 20Z" fill="var(--blue)"/></svg>
</div>

<!-- Envelope front 2 -->
<div class="sheet envelope" style="top:292px">
  <div class="brand" style="position:absolute;left:10px;top:9px"><span class="mark" style="width:9px;height:9px"></span><span class="name" style="font-size:9px">BRV</span></div>
  <div class="contact" style="left:10px;top:22px">742 Larkfield Road Edison, NJ 08841</div>
  <svg class="wave" viewBox="0 0 290 24" height="24" preserveAspectRatio="none"><path d="M0 4 Q120 26 290 16 L290 24 L0 24Z" fill="var(--steel)"/><path d="M0 10 Q110 28 230 24 L0 24Z" fill="var(--navy)"/></svg>
</div>
<div class="label" style="left:816px;top:376px;width:365px">Envelopes front and back</div>

</body>
</html>
```